Faithful Harbor Fellowship Network needs a fresh new web design

We are an up and coming multicultural church that aims to bring people into a life changing encounter with God. We need a fresh and inviting website in order to increase our internet presence and make us easier to connect with.
Here are some of the basic requirements for the site:
• Clearly displayed address, service times, and contact info
• A staff profile page
• An area for a calendar with upcoming events and their details
• Social media buttons
• Group pages for the different ministries (youth, children’s church, men, etc…)
• An area for donations and eCommerce
• A resources page for assorted media (podcasts, sermons, videos, etc.…)
• An area for prayer requests.

Industry/Entity Type

Church

```html
<!DOCTYPE html>
<html lang="en">
<head>
<meta charset="utf-8">
<title>Faithful Harbor Fellowship Network</title>
<link href="https://fonts.googleapis.com/css2?family=Noto+Serif:ital,wght@0,400;0,700;1,400&family=Noto+Sans:wght@400;700&family=Arimo:wght@400;700&display=swap" rel="stylesheet">
<style>
:root{
  --purple:#2b0a78;
  --purple-link:#2a1491;
  --blue:#2f6fd0;
  --blue-deep:#1d4fb0;
  --yellow:#fcc419;
  --light:#f4f4f4;
  --dark:#3a3a3a;
  --darker:#2c2c2c;
  --rule:#4c4c4c;
  --text:#222;
  --muted:#cfcfcf;
}
*{box-sizing:border-box;margin:0;padding:0}
html,body{width:865px;height:1200px;overflow:hidden;background:#fff}
body{font-family:"Noto Sans",sans-serif;color:var(--text);position:relative}
.wrap{width:754px;margin:0 auto;position:relative;height:100%}
a{color:var(--purple-link);text-decoration:none}

/* header */
.site-header{height:62px;background:#fff}
.brand{position:absolute;left:0;top:17px;display:flex;align-items:center;gap:7px;font-family:"Noto Serif",serif;font-size:12.5px;font-weight:700;color:var(--purple);line-height:1.15;width:190px}
.brand-mark{width:26px;height:26px;border-radius:50%;background:var(--purple);flex:none}
.main-nav{position:absolute;left:278px;top:0;display:flex;height:62px;font-size:10px;color:#333}
.main-nav a{color:#333;display:flex;align-items:center;padding:0 14px;height:62px}
.main-nav a.active{background:var(--purple);color:#fff;padding:0 15px}

/* hero */
.hero{height:318px;background:linear-gradient(to bottom,var(--blue-deep) 0,var(--blue) 70px,#2a66c8 232px,var(--yellow) 232px,var(--yellow) 318px)}
.slider{position:absolute;left:-1px;top:22px;width:756px;height:270px;background:#fff;border-radius:3px;box-shadow:0 6px 12px rgba(0,0,0,.25)}
.slide{position:absolute;left:8px;top:8px;width:736px;height:232px;background:radial-gradient(circle at 72% 45%,#c58a72 0,#7c4f57 22%,#3b2233 48%,#bfa2b7 80%,#e9d6de 100%)}
.caption{position:absolute;left:0;top:138px;width:354px;height:55px;background:rgba(110,110,110,.78);color:#fff;padding:6px 20px}
.caption h2{font-family:"Noto Sans",sans-serif;font-weight:400;font-size:11.5px;margin-bottom:4px}
.caption p{font-family:Arimo,sans-serif;font-size:7.5px;line-height:1.5}
.dots{position:absolute;left:349px;top:252px;display:flex;gap:1px}
.dots span{width:8px;height:8px;border-radius:50%;background:#9a9a9a;border:1px solid #777}
.dots span.on{background:#555}

/* features */
.features{height:230px;background:#fff}
.features .wrap{display:flex;justify-content:space-between;padding-top:20px}
.feature{width:234px}
h3.section-title{font-family:"Noto Serif",serif;font-weight:400;font-size:17px;color:#111;margin-bottom:12px}
.feature .media{height:116px;margin-bottom:15px}
.feature p{font-size:9.8px;line-height:1.6}
.media-church{background:linear-gradient(to bottom,#b9cfe8 0,#dfe7ef 40%,#8e3b2e 60%,#6b4a3c 100%)}
.media-video{background:linear-gradient(to bottom,#2a2a34 0,#4a4a5a 40%,#6b5a4f 100%);position:relative}
.media-video svg{position:absolute;left:89px;top:40px}
.media-welcome{background:linear-gradient(to right,#cfd6dc 0,#5a5a5e 35%,#3c3c40 55%,#e6e8ea 85%,#fff 100%)}

/* posts */
.posts{height:178px;background:var(--light)}
.posts .wrap{display:flex;justify-content:space-between;padding-top:18px}
.post-col{width:364px}
.post{display:flex;gap:16px}
.post .thumb{width:131px;height:103px;flex:none}
.thumb-rings{background:linear-gradient(135deg,#f3d9c3 0,#d79b5b 50%,#f1dcc8 100%)}
.thumb-stage{background:radial-gradient(circle at 50% 40%,#5a7f8f 0,#1d4555 50%,#0c1c24 100%)}
.post h4{font-weight:400;font-size:12.3px;color:var(--purple-link);margin:4px 0 9px}
.post p{font-size:9.8px;line-height:1.55}

/* verse */
.verse{height:69px;background:var(--purple);color:#fff}
.verse .wrap{display:flex;align-items:center;height:100%}
.verse-ref{font-size:12.5px;width:56px}
.verse-brace{font-family:"Noto Serif",serif;font-size:24px;width:50px;padding-left:19px}
.verse-text{font-family:"Noto Serif",serif;font-style:italic;font-size:11px;line-height:1.55;flex:1}

/* connect + footer */
.connect{height:187px;background:var(--dark);border-top:1px solid #555}
.connect .wrap,.site-footer .wrap{display:flex;justify-content:space-between;padding-top:20px}
.col{width:233px;font-family:Arimo,sans-serif;font-size:9.3px;color:var(--muted);line-height:1.6}
.col h5{font-family:"Noto Serif",serif;font-weight:400;font-size:14.5px;color:#cfcfcf;padding-bottom:6px;border-bottom:1px solid var(--rule);margin-bottom:9px}
.col > p{padding-left:2px}
.gallery{display:flex;justify-content:space-between;margin-top:10px}
.gallery div{width:69px;height:68px;background:radial-gradient(circle at 55% 40%,#b27a70 0,#4a2e42 55%,#c9a6c0 100%)}
.social{list-style:none;margin-top:8px}
.social li{display:flex;align-items:center;gap:11px;height:28px}
.dot{width:20px;height:20px;border-radius:50%;background:#d6d6d6;flex:none}
.email-field{margin-top:11px;width:206px;height:28px;background:#fff;border:1px solid #ccc;color:#aaa;font-size:9px;padding:8px 9px}
.pray-btn{margin-top:10px;width:87px;height:25px;background:var(--yellow);color:#fff;font-family:"Noto Serif",serif;font-weight:700;font-size:8px;display:flex;align-items:center;justify-content:center;border-radius:2px}
.site-footer{height:156px;background:var(--darker)}
.site-footer .wrap{padding-top:19px}
.col dt{color:#fff}
.col dd a,.col a.more{color:var(--yellow)}
.schedule{border-collapse:collapse;margin-top:0}
.schedule td{padding:0 9px 0 0;height:14.6px}
.more{display:block;margin-top:4px}
.donate{display:flex;align-items:center;gap:11px;margin-top:3px}
</style>
</head>
<body>

<header class="site-header">
  <div class="wrap">
    <div class="brand"><span class="brand-mark"></span><span>Faithful Harbor Fellowship Network</span></div>
    <nav class="main-nav">
      <a class="active" href="#">Home</a>
      <a href="#">About</a>
      <a href="#">News</a>
      <a href="#">Services</a>
      <a href="#">Ministries</a>
      <a href="#">Music &amp; Arts</a>
      <a href="#">Contact</a>
    </nav>
  </div>
</header>

<section class="hero">
  <div class="wrap">
    <div class="slider">
      <div class="slide" role="img" aria-label="Worship leader singing into a microphone on stage">
        <div class="caption">
          <h2>Vestibulum tincidunt feugiat consectetur.</h2>
          <p>Phasellus a velit porta lacus sollicitudin viverra. Duis eu egestas orci. Curabitur aliquet est in nisl malesuada feugiat. Pellentesque habitant morbi tristique senectus</p>
        </div>
      </div>
      <div class="dots"><span></span><span></span><span></span><span class="on"></span><span></span></div>
    </div>
  </div>
</section>

<section class="features">
  <div class="wrap">
    <div class="feature">
      <h3 class="section-title">Service Times &amp; Location</h3>
      <div class="media media-church" role="img" aria-label="Red brick church building with white columns"></div>
      <p>You are invited THIS SUNDAY for great music and preaching! <a href="#">Learn more »</a></p>
    </div>
    <div class="feature">
      <h3 class="section-title">Welcome Video</h3>
      <div class="media media-video" role="img" aria-label="Congregation gathered in a church auditorium, video still">
        <svg width="56" height="36" viewBox="0 0 56 36"><rect width="56" height="36" rx="7" fill="rgba(255,255,255,.55)"/><polygon points="22,9 22,27 37,18" fill="#111"/></svg>
      </div>
      <p>Watch this video to learn more about our church. <a href="#">Watch Video »</a></p>
    </div>
    <div class="feature">
      <h3 class="section-title">Welcome Center</h3>
      <div class="media media-welcome" role="img" aria-label="Speaker with outstretched arm addressing a crowd"></div>
      <p>Everything you need to know in one easy spot! <a href="#">Visit the Welcome Center »</a></p>
    </div>
  </div>
</section>

<section class="posts">
  <div class="wrap">
    <div class="post-col">
      <h3 class="section-title">Pastor's Blog</h3>
      <article class="post">
        <div class="thumb thumb-rings" role="img" aria-label="Two gold wedding rings on a printed page"></div>
        <div>
          <h4>5 Tips for a Blessed Marriage</h4>
          <p>Lorem ipsum dolor sit amet, consectetuer adipi-scing elit, sed diam nonummy nibh euismod tinc-idunt ut laoreet dolor, sed diam nonummy nibh euismod tincidunt ut laoreet...<br><a href="#">Read more »</a></p>
        </div>
      </article>
    </div>
    <div class="post-col">
      <h3 class="section-title">News &amp; Events</h3>
      <article class="post">
        <div class="thumb thumb-stage" role="img" aria-label="Musician singing on a stage with teal lights"></div>
        <div>
          <h4>Youth Lock-In happens next Saturday</h4>
          <p>Lorem ipsum dolor sit amet, consectetuer adipi-scing elit, sed diam nonummy nibh euismod tinc-idunt ut laoreet dolor, sed diam nonummy nibh euismod tincidunt ut laoreet...<br><a href="#">Read more »</a></p>
        </div>
      </article>
    </div>
  </div>
</section>

<section class="verse">
  <div class="wrap">
    <div class="verse-ref">Micah 6:8</div>
    <div class="verse-brace">}</div>
    <p class="verse-text">He has told you, O mortal, what is good; and what does the Lord require of you but to do justice, and to love kindness, and to walk humbly with your God?</p>
  </div>
</section>

<section class="connect">
  <div class="wrap">
    <div class="col">
      <h5>Photo Gallery</h5>
      <p>Stay connected for the latest updates at Cedar Grove Community Church.</p>
      <div class="gallery">
        <div role="img" aria-label="Worship leader with guitar"></div>
        <div role="img" aria-label="Worship leader with guitar"></div>
        <div role="img" aria-label="Worship leader with guitar"></div>
      </div>
    </div>
    <div class="col">
      <h5>Contact Us</h5>
      <p>Stay connected for the latest updates at Cedar Grove Community Church.</p>
      <ul class="social">
        <li><span class="dot"></span>like us on ConnectPage</li>
        <li><span class="dot"></span>follow us on ChirpLine</li>
      </ul>
    </div>
    <div class="col">
      <h5>Request for prayer</h5>
      <p>You can request us to pray for you by providing your email, we will contact you.</p>
      <div class="email-field">E-mail Address</div>
      <div class="pray-btn">PRAY FOR ME</div>
    </div>
  </div>
</section>

<footer class="site-footer">
  <div class="wrap">
    <div class="col">
      <h5>Cedar Grove Community Church</h5>
      <dl>
        <dt>Address</dt>
        <dd>Name of The Street, TheCity, [TS] 98765 <a href="#">(map)</a></dd>
        <dt>Phone</dt>
        <dd>555-014-2290</dd>
        <dd>E-mail</dd>
        <dd><a href="#">hello@faithfulharbor.net</a></dd>
      </dl>
    </div>
    <div class="col">
      <h5>Sunday Service Schedule</h5>
      <table class="schedule">
        <tr><td style="color:#fff">08:30 am</td><td>Traditional Service</td></tr>
        <tr><td style="color:#fff">09:45 am</td><td>Sunday School</td></tr>
        <tr><td style="color:#fff">11:00 am</td><td>Contemporary Service</td></tr>
        <tr><td style="color:#fff">11:00 am</td><td>Traditional Service</td></tr>
      </table>
      <a class="more" href="#">more detail</a>
    </div>
    <div class="col">
      <h5>Donate for Us</h5>
      <div class="donate"><span class="dot"></span>GivePort</div>
    </div>
  </div>
</footer>

</body>
</html>
```